For Sale

Tidewell Realty Guam
Please call Corinne Halvorsen
(671) 555-2139

Target Market(s)

Buyer and renter

Industry/Entity Type

Real Estate

Font styles to use
Serif
Sans Serif

Colors
0054AA
0677BA
7BADD7
CADEEF
E8F1F8

Requirements
Must have
• Client attention once see the sign
Nice to have
• Island theme

```html
<!DOCTYPE html>
<html lang="en">
<head>
<meta charset="utf-8">
<title>Tidewell Realty Guam – Yard Signs</title>
<link rel="stylesheet" href="https://fonts.googleapis.com/css2?family=Archivo+Black&family=Cinzel:wght@500&display=swap">
<style>
  :root {
    --sign-blue: #1a95d4;
    --panel-white: #ffffff;
    --phone-orange: #fbae3f;
    --photo-light: #6d8fb8;
    --photo-dark: #4a3226;
  }
  html, body {
    margin: 0;
    padding: 0;
    overflow: hidden;
    background: var(--panel-white);
  }
  .canvas {
    position: relative;
    width: 1019px;
    height: 1200px;
    overflow: hidden;
    background: var(--panel-white);
  }
  .sign {
    position: absolute;
    left: 0;
    width: 1019px;
    height: 585px;
    background: var(--sign-blue);
  }
  .sign--sale { top: 0; }
  .sign--lease { top: 615px; }
  .sign__panel {
    position: absolute;
    left: 27px;
    top: 27px;
    width: 966px;
    height: 353px;
    background: var(--panel-white);
  }
  .agent-photo {
    position: absolute;
    left: 19px;
    top: 10px;
    width: 212px;
    height: 212px;
    box-sizing: border-box;
    border-radius: 50%;
    border: 4px solid var(--sign-blue);
    background: radial-gradient(circle at 50% 40%, var(--photo-light) 0%, var(--photo-light) 45%, var(--photo-dark) 100%);
  }
  .brand-name {
    position: absolute;
    left: 300px;
    top: 55px;
    width: 380px;
    margin: 0;
    text-align: center;
    font-family: "Cinzel", serif;
    font-weight: 500;
    color: var(--sign-blue);
    line-height: 1.05;
  }
  .brand-name__main { display: block; font-size: 66px; letter-spacing: 2px; }
  .brand-name__sub { display: block; font-size: 28px; letter-spacing: 10px; margin-top: 12px; }
  .sign__headline,
  .sign__phone {
    position: absolute;
    left: 0;
    width: 1019px;
    overflow: visible;
  }
  .sign__headline { top: 0; height: 380px; }
  .sign__phone { top: 380px; height: 205px; }
  .headline-text {
    font-family: "Archivo Black", sans-serif;
    fill: var(--sign-blue);
  }
  .phone-text {
    font-family: "Archivo Black", sans-serif;
    fill: var(--phone-orange);
  }
</style>
</head>
<body>
<main class="canvas">

  <section class="sign sign--sale">
    <div class="sign__panel">
      <div class="agent-photo" role="img" aria-label="Portrait photo of agent Corinne Halvorsen"></div>
      <p class="brand-name">
        <span class="brand-name__main">Tidewell</span>
        <span class="brand-name__sub">Realty Guam</span>
      </p>
    </div>
    <svg class="sign__headline" viewBox="0 0 1019 380">
      <text class="headline-text" x="91" y="375" font-size="169" textLength="839" lengthAdjust="spacingAndGlyphs">FOR SALE</text>
    </svg>
    <svg class="sign__phone" viewBox="0 0 1019 205">
      <text class="phone-text" x="61" y="145" font-size="113" textLength="860" lengthAdjust="spacingAndGlyphs">(671)555-2139</text>
    </svg>
  </section>

  <section class="sign sign--lease">
    <div class="sign__panel">
      <div class="agent-photo" role="img" aria-label="Portrait photo of agent Corinne Halvorsen"></div>
      <p class="brand-name">
        <span class="brand-name__main">Tidewell</span>
        <span class="brand-name__sub">Realty Guam</span>
      </p>
    </div>
    <svg class="sign__headline" viewBox="0 0 1019 380">
      <text class="headline-text" x="33" y="375" font-size="169" textLength="955" lengthAdjust="spacingAndGlyphs">FOR LEASE</text>
    </svg>
    <svg class="sign__phone" viewBox="0 0 1019 205">
      <text class="phone-text" x="61" y="145" font-size="113" textLength="860" lengthAdjust="spacingAndGlyphs">(671)555-2139</text>
    </svg>
  </section>

</main>
</body>
</html>
```